Fahrzeugbeschriftung für Sanitätshaus
Zielgruppe
Wir als Mobil-Service nah sind ein Sanitätshaus und beliefern unsere Kunden mit allen gängigen Hilfsmitteln wie z.B. Rollatoren, Rollstühle, Hilfen für das Badezimmer oder Pflegebetten. Unser Unternehmen existiert seit 20 Jahren und unsere Zielgruppe sind ältere, hilfsbedürftige und kranke Menschen. Unsere Kunden sind in der Regel zwischen 50 und 80 Jahre alt. Aber auch Kinder gehören zu unseren Kunden.
Wir arbeiten in partnerschaftlichem Verhältnis mit Ärzten, Krankenhäusern, Pflegediensten und Pflegeeinrichtungen sowie Kostenträgern, Lieferanten und sonstigen Geschäftspartnern.
Wir sind auf der Suche nach einer hochwertigen Fahrzeugbeschriftung für unsere Lieferfahrzeuge. Wir möchten gerne zeigen wer wir sind und was wir machen. Wir möchten auf unseren täglichen Touren mehr auf uns aufmerksam machen und im Besten Fall dadurch Neukunden gewinnen. Aber auch der Wiedererkennungswert unseres Unternehmens soll damit gesteigert werden. Wir möchten zeigen, dass wir DAS Sanitätshaus in der Region sind.
Aufgabenstellung
Wir möchten zeigen wo unsere Firma ihren Sitz hat und was wir machen. Es sollte also unsere Adresse und unsere Kontaktdaten zu sehen sein. Es sollte erkennbar sein, dass wir ein Sanitätshaus sind. Entweder durch geläufige Begriffe wie Rollator, Rollstuhl, Pflegebett, Dusch- und Toilettenhilfen, Sauerstoffversorgung oder unterstützt durch Bilder.
Unser Zielgruppe sind ältere Menschen, daher sollte das Design nicht zu jugendlich/flippig sein sondern eher ruhig und gediegen. Es sollte aber auf jeden Fall auch modern sein um sich von unseren Mitbewerbern abzuheben. Es muss aber auch alltagstauglich sein, da wir nicht nur zu unseren Endkunden nach Hause fahren sondern auch zu Pflegeheimen und Krankenhäusern. Und dort ist es oft sehr konservativ und elitär.
Wir haben keine social Media Seiten. Aber unsere Webseite sollte benannt werden.
Unsere Autos sind weiß bzw. silber. Unser Logo besteht aus den Farben grau und blau. Diese Farben sollten verwendet werden.
Unsere Fahrzeige sind:
- Velmo Kargon Kasten 350 L2H2, Baujahr 2022
- Velmo Kargon Linka Kasten 220 L1 Trend, Baujahr 2022

```html
<!DOCTYPE html>
<html lang="de">
<head>
<meta charset="utf-8">
<title>Mobil-Service nah – Fahrzeugbeschriftung</title>
<link href="https://fonts.googleapis.com/css2?family=Arimo:ital,wght@0,400;0,700;1,700&display=swap" rel="stylesheet">
<style>
  :root {
    --backdrop: #c0d9fc;
    --brand-blue: #174ea0;
    --brand-grey: #7d817c;
    --body-white: #ffffff;
    --photo-blue: #5f88b8;
    --photo-warm: #c9ad8a;
    --photo-light: #dfe3e8;
    --photo-green: #6f8a52;
  }
  html, body {
    margin: 0;
    padding: 0;
    width: 1200px;
    height: 1200px;
    overflow: hidden;
    background: var(--backdrop);
  }
  .van-wrap {
    display: block;
    width: 1200px;
    height: 1200px;
    font-family: "Arimo", Arial, sans-serif;
  }
  .fill-white { fill: var(--body-white); }
  .fill-blue { fill: var(--brand-blue); }
  .fill-grey { fill: var(--brand-grey); }
  .fill-backdrop { fill: var(--backdrop); }
  .brand-name { fill: var(--brand-blue); font-weight: 400; font-size: 36px; }
  .headline { fill: var(--brand-blue); font-weight: 700; font-size: 32px; }
  .headline-em { font-style: italic; }
  .subline { fill: var(--brand-blue); font-weight: 700; font-size: 20px; }
  .phone-frame { fill: none; stroke: var(--brand-blue); stroke-width: 4; }
  .phone-number { fill: var(--brand-blue); font-weight: 700; font-size: 52px; }
  .range-title { fill: var(--body-white); font-weight: 700; font-size: 46px; }
  .range-item { fill: var(--body-white); font-weight: 400; font-size: 13px; }
  .tick-ring { fill: none; stroke: var(--body-white); stroke-width: 1; }
  .tick-mark { fill: none; stroke: var(--body-white); stroke-width: 1.2; }
</style>
</head>
<body>
<svg class="van-wrap" viewBox="0 0 1932 1932" xmlns="http://www.w3.org/2000/svg">
  <defs>
    <clipPath id="van-body-clip">
      <path d="M200,1060 L205,1010 Q225,935 340,905 Q390,890 420,870 L700,625 Q800,540 920,532 L1640,515 Q1662,520 1672,600 L1697,855 L1672,1027 L1510,1032 Q1420,985 1330,1060 Q1308,1100 1305,1145 L550,1160 Q545,1080 480,1040 Q400,1005 330,1055 Z"/>
    </clipPath>
    <polygon id="hex-frame" points="-76,0 -38,-66 38,-66 76,0 38,66 -38,66"/>
    <polygon id="hex-photo" points="-60,0 -30,-52 30,-52 60,0 30,52 -30,52"/>
  </defs>

  <g class="van-side" clip-path="url(#van-body-clip)">
    <rect class="fill-white" x="150" y="480" width="1600" height="720"/>

    <!-- lower blue swoosh -->
    <path class="fill-blue" d="M180,890 L340,905 L390,930 L375,948 L430,948 Q620,1030 900,1045 Q1100,1050 1270,1005 L1290,970 L1370,970 L1380,978 Q1520,935 1670,855 L1710,855 L1710,1200 L180,1200 Z"/>
    <!-- grey rocker band -->
    <path class="fill-grey" d="M190,1015 L335,1005 L480,1040 Q900,1110 1330,1065 Q1500,1010 1680,945 L1710,1200 L190,1200 Z"/>

    <!-- headlight -->
    <path class="fill-white" d="M215,1010 Q230,950 335,925 Q295,960 283,1000 Q240,995 215,1010 Z"/>

    <!-- side window and door hardware -->
    <path class="fill-backdrop" d="M378,945 Q480,830 605,740 Q640,722 725,720 L717,855 Q715,880 680,895 Q580,935 430,948 Z"/>
    <rect class="fill-backdrop" x="679" y="928" width="68" height="13" rx="6"/>
    <circle class="fill-backdrop" cx="710" cy="934" r="13"/>
    <circle class="fill-backdrop" cx="710" cy="1000" r="8"/>

    <!-- rear honeycomb accents -->
    <use href="#hex-frame" class="fill-grey" transform="translate(1455,515)"/>
    <use href="#hex-frame" class="fill-grey" transform="translate(1455,955)"/>
    <use href="#hex-frame" class="fill-blue" transform="translate(1725,660)"/>
    <use href="#hex-frame" class="fill-grey" transform="translate(1725,805)"/>

    <g class="product-hex">
      <use href="#hex-frame" class="fill-blue" transform="translate(1323,587)"/>
      <use href="#hex-photo" fill="var(--photo-light)" transform="translate(1323,587)" role="img" aria-label="Foto: Rollstuhlfahrer in heller Wohnung"/>
    </g>
    <g class="product-hex">
      <use href="#hex-frame" class="fill-blue" transform="translate(1327,735)"/>
      <use href="#hex-photo" fill="var(--body-white)" transform="translate(1327,735)" role="img" aria-label="Foto: Rollator"/>
    </g>
    <g class="product-hex">
      <use href="#hex-frame" class="fill-blue" transform="translate(1329,885)"/>
      <use href="#hex-photo" fill="var(--photo-green)" transform="translate(1329,885)" role="img" aria-label="Foto: Frau im Rollstuhl auf einer Weide"/>
    </g>
    <g class="product-hex">
      <use href="#hex-frame" class="fill-blue" transform="translate(1457,660)"/>
      <use href="#hex-photo" fill="var(--photo-warm)" transform="translate(1457,660)" role="img" aria-label="Foto: Pflegebett im Zimmer"/>
    </g>
    <g class="product-hex">
      <use href="#hex-frame" class="fill-blue" transform="translate(1458,810)"/>
      <use href="#hex-photo" fill="var(--photo-blue)" transform="translate(1458,810)" role="img" aria-label="Foto: Dusche mit Haltegriff"/>
    </g>
    <g class="product-hex">
      <use href="#hex-frame" class="fill-blue" transform="translate(1586,584)"/>
      <use href="#hex-photo" fill="var(--body-white)" transform="translate(1586,584)" role="img" aria-label="Foto: Rollstuhl"/>
    </g>
    <g class="product-hex">
      <use href="#hex-frame" class="fill-blue" transform="translate(1588,731)"/>
      <use href="#hex-photo" fill="var(--body-white)" transform="translate(1588,731)" role="img" aria-label="Foto: Sauerstoffkonzentrator"/>
    </g>
    <g class="product-hex">
      <use href="#hex-frame" class="fill-blue" transform="translate(1590,880)"/>
      <use href="#hex-photo" fill="var(--photo-light)" transform="translate(1590,880)" role="img" aria-label="Foto: Elektromobil"/>
    </g>
  </g>

  <!-- brand and message -->
  <text class="brand-name" x="995" y="630" text-anchor="middle">Mobil-Service nah</text>

  <text class="headline" x="992" y="715" text-anchor="middle">DAS <tspan class="headline-em">SANITÄTSHAUS</tspan></text>
  <text class="subline" x="980" y="742" text-anchor="middle">► IN DER REGION SIND. ◄</text>

  <rect class="phone-frame" x="805" y="764" width="358" height="68" rx="34"/>
  <text class="phone-number" x="984" y="817" text-anchor="middle">04321-558270</text>

  <g class="product-range">
    <path class="fill-blue" d="M820,1032 L820,880 Q820,855 845,855 L1127,855 Q1152,855 1152,880 L1152,1017 Q1000,1035 820,1032 Z"/>
    <text class="range-title" x="992" y="914" text-anchor="middle">HILFSMITTEL</text>

    <g class="range-col">
      <circle class="tick-ring" cx="863" cy="938" r="5"/><path class="tick-mark" d="M860.5,938 l2,2 l3,-4"/>
      <text class="range-item" x="875" y="943">Bad und Toilette</text>
      <circle class="tick-ring" cx="863" cy="954" r="5"/><path class="tick-mark" d="M860.5,954 l2,2 l3,-4"/>
      <text class="range-item" x="875" y="959">Bewegungstrainer</text>
      <circle class="tick-ring" cx="863" cy="970" r="5"/><path class="tick-mark" d="M860.5,970 l2,2 l3,-4"/>
      <text class="range-item" x="875" y="975">Elektromobil</text>
      <circle class="tick-ring" cx="863" cy="986" r="5"/><path class="tick-mark" d="M860.5,986 l2,2 l3,-4"/>
      <text class="range-item" x="875" y="991">Gehhilfen</text>
      <circle class="tick-ring" cx="863" cy="1003" r="5"/><path class="tick-mark" d="M860.5,1003 l2,2 l3,-4"/>
      <text class="range-item" x="875" y="1008">Matratzen</text>
    </g>
    <g class="range-col">
      <circle class="tick-ring" cx="1027" cy="940" r="5"/><path class="tick-mark" d="M1024.5,940 l2,2 l3,-4"/>
      <text class="range-item" x="1040" y="945">Pflegebetten</text>
      <circle class="tick-ring" cx="1027" cy="956" r="5"/><path class="tick-mark" d="M1024.5,956 l2,2 l3,-4"/>
      <text class="range-item" x="1040" y="961">Rollstühle</text>
      <circle class="tick-ring" cx="1027" cy="972" r="5"/><path class="tick-mark" d="M1024.5,972 l2,2 l3,-4"/>
      <text class="range-item" x="1040" y="976">Sauerstoff</text>
      <circle class="tick-ring" cx="1027" cy="988" r="5"/><path class="tick-mark" d="M1024.5,988 l2,2 l3,-4"/>
      <text class="range-item" x="1040" y="992">Zusatzantriebe</text>
    </g>
  </g>
</svg>
</body>
</html>
```